Harborline Network Solutions - IT Services Company/Managed Services/Consulting Card Design

Our company needs a business card design that will appeal to client companies with 50-1000 employees. We do IT services, administration, management, projects, budgeting and consulting (Like a small Quellbrook.com, Vantrelle.com or Drumvale.com). Mainly helping businesses use technology to be more competitive and efficient. We work with IT Infrastructure, switches, routers, firewalls and Cloud, Penwick/Tarvo servers, Kelpnode server virtualization, Datacenter environments, Email systems, Business Systems, Backup, Disaster Recovery, Data Security, ZPB, Workdesk 720 and Mistral.) Would like the final design to be professional but stand out to our prospective clients. Our current logo is attached. Color or design could be changed. Overall looking for a great finished product, original ideas are welcome and would pay more for the right one. If you think you have a better logo idea include a general idea if you can. Web design has not been done yet so that is a later possibility too.

Target Market(s)

1st - Mid-sized companies with 100-1000 employees with technology needs
2nd - Smaller companies with 20-99 employees with technology needs
- These companies can be in many different industries. Heathcare, legal, manufacturing, education, non-profit, services

Industry/Entity Type

Information Technology

Contact Information for Business Card

Should include the following info:

Logo or other logo with Company Name

Martin J. Calder

Principal

HarborlineNet.example

mcalder@HarborlineNet.example

(555) 7-HARBOR x 318

Font styles to use
Other font styles liked:
• designer can decide

Requirements
Must have
• Professional, appealing design, appeal to the target market
Nice to have
• Some sort of additional accent design that would stand out could be nice. I thought of adding a graphic in the top left corner that would look like the corner of the card was becoming more and more pixelated as it got near the corner, with some pixels missing.

```html
<!DOCTYPE html>
<html lang="en">
<head>
<meta charset="utf-8">
<title>Harborline Network Solutions – Business Card</title>
<link rel="stylesheet" href="https://fonts.googleapis.com/css2?family=Open+Sans:wght@400;600;700&display=swap">
<style>
  :root {
    --brand-blue: #1877c1;
    --card-white: #ffffff;
    --ink-dark: #1f2328;
    --stage: #eceff2;
    --shadow: rgba(20, 30, 45, 0.18);
  }
  * { box-sizing: border-box; margin: 0; padding: 0; }
  html, body {
    width: 1200px; height: 900px; overflow: hidden;
    background: var(--stage);
    font-family: "Open Sans", Arial, sans-serif;
  }
  .canvas { position: relative; width: 1200px; height: 900px; }
  .card {
    position: absolute; width: 560px; height: 320px;
    box-shadow: 0 10px 28px var(--shadow);
    overflow: hidden;
  }
  .card-back {
    left: 90px; top: 110px;
    background: var(--brand-blue);
    display: flex; align-items: center; justify-content: center;
  }
  .card-front {
    left: 550px; top: 440px;
    display: flex;
  }
  .company-name {
    font-weight: 600; letter-spacing: 0.02em; line-height: 1.2;
    text-align: center;
  }
  .card-back .company-name { color: var(--card-white); font-size: 30px; width: 340px; }
  .front-info {
    width: 292px; flex: none;
    background: var(--brand-blue); color: var(--card-white);
    padding: 44px 18px 30px 32px;
    display: flex; flex-direction: column; justify-content: space-between;
  }
  .person-name { font-weight: 700; font-size: 17px; }
  .person-title { font-size: 15px; margin-top: 2px; }
  .contact-list { list-style: none; font-size: 13px; line-height: 1.75; }
  .contact-list li { display: flex; align-items: center; gap: 7px; white-space: nowrap; }
  .contact-list svg { width: 11px; height: 11px; flex: none; }
  .front-logo {
    flex: 1; background: var(--card-white);
    display: flex; align-items: center; justify-content: center;
    padding: 0 22px;
  }
  .front-logo .company-name { color: var(--ink-dark); font-size: 23px; }
</style>
</head>
<body>
<main class="canvas">
  <section class="card card-back" aria-label="Card back">
    <p class="company-name">Harborline Network Solutions</p>
  </section>

  <section class="card card-front" aria-label="Card front">
    <div class="front-info">
      <div class="identity">
        <p class="person-name">Martin J. Calder</p>
        <p class="person-title">Principal</p>
      </div>
      <ul class="contact-list">
        <li>
          <svg viewBox="0 0 12 12" aria-hidden="true"><rect x="3" y="0.8" width="6" height="10.4" rx="1.2" fill="none" stroke="#fff" stroke-width="1.2"/><rect x="5" y="9" width="2" height="1" fill="#fff"/></svg>
          (555) 7-HARBOR x 318
        </li>
        <li>
          <svg viewBox="0 0 12 12" aria-hidden="true"><rect x="0.5" y="2" width="11" height="8" fill="#fff"/><path d="M0.5 2 L6 6.5 L11.5 2" fill="none" stroke="#1877c1" stroke-width="1"/></svg>
          mcalder@HarborlineNet.example
        </li>
        <li>
          <svg viewBox="0 0 12 12" aria-hidden="true"><circle cx="6" cy="6" r="5.5" fill="#fff"/><path d="M6 0.5 V11.5 M0.5 6 H11.5" stroke="#1877c1" stroke-width="0.8"/><ellipse cx="6" cy="6" rx="2.4" ry="5.5" fill="none" stroke="#1877c1" stroke-width="0.8"/></svg>
          www.HarborlineNet.example
        </li>
      </ul>
    </div>
    <div class="front-logo">
      <p class="company-name">Harborline Network Solutions</p>
    </div>
  </section>
</main>
</body>
</html>
```